Quivolt value proposition infographic

• Update to existing “Quivolt Features” wheel infographic (attached) to be more value proposition focused rather than feature focused.
• We want something fresh and new.
• Content messaging to be the 5 value prop points:
1. Intelligent Payment Capture
2. MultiSplit Payouts
3. Ultra Partnerships
4. NextGen Technology Platform
5. Unrivalled Geographical Coverage
• New artwork to appear on Quivolt assets –quivolt.com, business cards, proposal documents etc. – new artwork will need to be scalable.
• Layout is not locked into being a circle, but other design/layout elements of our website/brand should be considered when redesigning this artwork
• Guidelines and brand assets can be found here: https://www.quivolt.com/promotional-guidelines
• Deliverables: Visual file to use in online and offline marketing campaigns. File types: (in CYMK and/or RGB where applicable) .jpg, .png, EPS, PDF
• Tone and image: Functional, engaging, informative, energetic, accessible.
• We want our audience need to understand Quivolt’s total payment expertise focusing on the 5 points of value (listed below in ‘Messages’). They should want to seek more information on the Quivolt value drivers either through continued navigation through our website or contacting our team.

Target Market(s)

Companies searching for recurring payment proviers

Colors
0054AA
0677BA
7BADD7
CADEEF
E8F1F8
F0912C
F2A743
F7CA91
FBE8D2
FDF5EE

Requirements
Should not have
• The same design replacing the old wording with new words.

```html
<!DOCTYPE html>
<html lang="en">
<head>
<meta charset="utf-8">
<title>Quivolt Value Proposition</title>
<link href="https://fonts.googleapis.com/css2?family=Open+Sans:wght@800&display=swap" rel="stylesheet">
<style>
  :root {
    --bg: #ffffff;
    --ink: #0a2540;
    --navy: #0054AA;
    --blue: #0677BA;
    --sky: #7BADD7;
    --mist: #CADEEF;
    --ice: #E8F1F8;
    --orange: #F0912C;
    --amber: #F2A743;
    --peach: #F7CA91;
    --sand: #FBE8D2;
    --cream: #FDF5EE;
  }
  html, body {
    margin: 0;
    padding: 0;
    overflow: hidden;
    background: var(--bg);
  }
  .canvas {
    position: relative;
    width: 1200px;
    height: 1185px;
    overflow: hidden;
    background: var(--bg);
  }
  .value-wheel {
    position: absolute;
    left: 0;
    top: 0;
    width: 1200px;
    height: 1185px;
  }
  .value-label {
    position: absolute;
    margin: 0;
    font-family: "Open Sans", Arial, sans-serif;
    font-weight: 800;
    font-size: 20px;
    line-height: 24px;
    letter-spacing: 0.3px;
    text-transform: uppercase;
    color: var(--ink);
    white-space: nowrap;
  }
  .value-label--left { text-align: right; }
  .value-label--right { text-align: left; }
  .value-label--bottom { text-align: center; transform: translateX(-50%); }
  .label-capture { right: 810px; top: 384px; }
  .label-payouts { left: 810px; top: 396px; }
  .label-partnerships { right: 890px; top: 689px; }
  .label-platform { left: 890px; top: 677px; }
  .label-coverage { left: 600px; top: 908px; }
</style>
</head>
<body>
<main class="canvas">
  <svg class="value-wheel" viewBox="0 0 1200 1185" aria-label="Five Quivolt value propositions arranged around a ring">
    <circle class="wheel-glow" cx="600" cy="620" r="292" fill="var(--cream)"/>
    <circle class="wheel-orbit" cx="600" cy="620" r="272" fill="none" stroke="var(--sand)" stroke-width="2" stroke-dasharray="3 9" stroke-linecap="round"/>

    <g class="wheel-segments">
      <path class="segment segment-payouts" fill="var(--blue)"
        d="M608.7 370.1 A250 250 0 0 1 834.9 534.5 L755.1 563.6 A165 165 0 0 0 605.8 455.1 Z"/>
      <path class="segment segment-platform" fill="var(--sky)"
        d="M840.3 551.1 A250 250 0 0 1 753.9 817 L701.6 750 A165 165 0 0 0 758.6 574.5 Z"/>
      <path class="segment segment-coverage" fill="var(--orange)"
        d="M739.8 827.3 A250 250 0 0 1 460.2 827.3 L507.7 756.8 A165 165 0 0 0 692.3 756.8 Z"/>
      <path class="segment segment-partnerships" fill="var(--amber)"
        d="M446.1 817 A250 250 0 0 1 359.7 551.1 L441.4 574.5 A165 165 0 0 0 498.4 750 Z"/>
      <path class="segment segment-capture" fill="var(--navy)"
        d="M365.1 534.5 A250 250 0 0 1 591.3 370.1 L594.2 455.1 A165 165 0 0 0 444.9 563.6 Z"/>
    </g>

    <g class="wheel-hub">
      <circle cx="600" cy="620" r="145" fill="var(--ice)"/>
      <circle cx="600" cy="620" r="108" fill="#ffffff"/>
      <circle cx="600" cy="620" r="84" fill="none" stroke="var(--mist)" stroke-width="10"/>
      <circle cx="600" cy="620" r="84" fill="none" stroke="var(--peach)" stroke-width="10" stroke-dasharray="90 438" stroke-linecap="round" transform="rotate(20 600 620)"/>
      <circle cx="600" cy="620" r="44" fill="var(--sand)"/>
      <circle cx="600" cy="620" r="18" fill="var(--orange)"/>
    </g>

    <g class="wheel-leaders" stroke-width="2" fill="none">
      <line x1="446" y1="408" x2="402" y2="408" stroke="var(--navy)"/>
      <line x1="754" y1="408" x2="798" y2="408" stroke="var(--blue)"/>
      <line x1="849" y1="701" x2="878" y2="701" stroke="var(--sky)"/>
      <line x1="351" y1="701" x2="322" y2="701" stroke="var(--amber)"/>
      <line x1="600" y1="882" x2="600" y2="898" stroke="var(--orange)"/>
    </g>
    <g class="wheel-markers">
      <circle cx="446" cy="408" r="6" fill="var(--navy)"/>
      <circle cx="754" cy="408" r="6" fill="var(--blue)"/>
      <circle cx="849" cy="701" r="6" fill="var(--sky)"/>
      <circle cx="351" cy="701" r="6" fill="var(--amber)"/>
      <circle cx="600" cy="882" r="6" fill="var(--orange)"/>
    </g>
  </svg>

  <p class="value-label value-label--left label-capture">Intelligent Payment<br>Capture</p>
  <p class="value-label value-label--right label-payouts">Multisplit Payouts</p>
  <p class="value-label value-label--left label-partnerships">Ultra Partnerships</p>
  <p class="value-label value-label--right label-platform">NextGen Technology<br>Platform</p>
  <p class="value-label value-label--bottom label-coverage">Unrivalled Geographical<br>Coverage</p>
</main>
</body>
</html>
```